Car Detailing product label for 750ML Clear Bottle

I need a label for various product with differente color for each products but in the same size bottle each time. It's only for our purpose no commercial application. I need a template with differente color but same design. The name for product it's : Brisk Harbor. We dont have any logo because it's only for us. We like like car silhouette in the logo or in background or something like that.

And for the product we have many like : APC Cleaner, Drying Aid, Wheel Cleaner and some other.

Font styles to use
Serif
Sans Serif

```html
<!DOCTYPE html>
<html lang="en">
<head>
<meta charset="utf-8">
<title>Brisk Harbor – 750ml Label Templates</title>
<link rel="stylesheet" href="https://fonts.googleapis.com/css2?family=Bebas+Neue&family=Open+Sans:wght@700&display=swap">
<style>
  :root {
    --page: #f4f4f4;
    --label-black: #050505;
    --pattern-grey: #161616;
    --ink: #0a0a0a;
    --white: #ffffff;
    --red: #ed1c24;
    --lime: #9fba3c;
    --purple: #9b4fa0;
    --pink: #ea7f8f;
    --green: #1e9a4a;
  }
  * { box-sizing: border-box; margin: 0; padding: 0; }
  html, body { width: 1200px; height: 800px; overflow: hidden; background: var(--page); }
  .canvas { position: relative; width: 1200px; height: 800px; }

  .label {
    position: absolute;
    background: var(--label-black);
    border-top: var(--band-top) solid var(--accent);
    border-bottom: var(--band-bottom) solid var(--accent);
    overflow: hidden;
  }
  .label__pattern {
    position: absolute; inset: 0;
    background: var(--pattern-grey);
  }
  .label__frame {
    position: absolute;
    border: 3px solid var(--accent);
    border-radius: var(--frame-radius);
    background: var(--label-black);
    padding: var(--frame-gap);
  }
  .label__frame-inner {
    width: 100%; height: 100%;
    border: 2px solid var(--white);
    border-radius: calc(var(--frame-radius) - 6px);
    display: flex; align-items: center; justify-content: center;
  }
  .brand-name {
    font-family: "Bebas Neue", "Arial Narrow", sans-serif;
    font-weight: 400;
    color: var(--white);
    text-align: center;
    line-height: 0.9;
    letter-spacing: 0.01em;
  }
  .label__volume {
    position: absolute; left: 0; right: 0;
    text-align: center;
    font-family: "Open Sans", Arial, sans-serif;
    font-weight: 700;
    color: var(--accent);
  }

  /* main label */
  .label--main {
    left: 145px; top: 56px; width: 595px; height: 447px;
    --band-top: 11px; --band-bottom: 16px;
    --frame-radius: 30px; --frame-gap: 8px;
  }
  .label--main .label__frame { left: 115px; top: 15px; width: 366px; height: 277px; }
  .label--main .brand-name { font-size: 100px; }
  .label--main .label__volume { top: 380px; font-size: 22px; }

  /* small labels */
  .label--small {
    width: 273px; height: 205px;
    --band-top: 5px; --band-bottom: 6px;
    --frame-radius: 16px; --frame-gap: 4px;
  }
  .label--small .label__frame { left: 53px; top: 8px; width: 168px; height: 125px; }
  .label--small .brand-name { font-size: 46px; }
  .label--small .label__volume { top: 175px; font-size: 11px; }

  .label--lime   { --accent: var(--lime);   left: 784px; top: 298px; }
  .label--purple { --accent: var(--purple); left: 145px; top: 540px; }
  .label--pink   { --accent: var(--pink);   left: 464px; top: 540px; }
  .label--green  { --accent: var(--green);  left: 784px; top: 540px; }
  .label--red    { --accent: var(--red); }

  /* standalone wordmark */
  .wordmark {
    position: absolute; left: 783px; top: 60px; width: 270px;
  }
  .wordmark .brand-name { color: var(--ink); font-size: 100px; }
</style>
</head>
<body>
<main class="canvas">

  <section class="label label--main label--red">
    <div class="label__pattern" role="img" aria-label="Faint repeating sports car silhouette pattern"></div>
    <div class="label__frame"><div class="label__frame-inner"><p class="brand-name">Brisk<br>Harbor</p></div></div>
    <p class="label__volume">750ml</p>
  </section>

  <div class="wordmark"><p class="brand-name">Brisk<br>Harbor</p></div>

  <section class="label label--small label--lime">
    <div class="label__pattern" role="img" aria-label="Faint repeating sports car silhouette pattern"></div>
    <div class="label__frame"><div class="label__frame-inner"><p class="brand-name">Brisk<br>Harbor</p></div></div>
    <p class="label__volume">750ml</p>
  </section>

  <section class="label label--small label--purple">
    <div class="label__pattern" role="img" aria-label="Faint repeating sports car silhouette pattern"></div>
    <div class="label__frame"><div class="label__frame-inner"><p class="brand-name">Brisk<br>Harbor</p></div></div>
    <p class="label__volume">750ml</p>
  </section>

  <section class="label label--small label--pink">
    <div class="label__pattern" role="img" aria-label="Faint repeating sports car silhouette pattern"></div>
    <div class="label__frame"><div class="label__frame-inner"><p class="brand-name">Brisk<br>Harbor</p></div></div>
    <p class="label__volume">750ml</p>
  </section>

  <section class="label label--small label--green">
    <div class="label__pattern" role="img" aria-label="Faint repeating sports car silhouette pattern"></div>
    <div class="label__frame"><div class="label__frame-inner"><p class="brand-name">Brisk<br>Harbor</p></div></div>
    <p class="label__volume">750ml</p>
  </section>

</main>
</body>
</html>
```